Letterhead design for Sleep Consulting Business

I'm looking for a new letterhead (heading/footer) design for my Sleep Consulting Business, I work with families to help their children improve their sleep.

The heading/footer will used in Microsoft Word Only-to be used for all of my documents such as writing Sleep Plans. I need to utilize as much working space in the document as possible. This will NOT be printed out on paper- it will only be used for heading/footer on microsoft word, then emailed to clients, who may print it at home.

My brand colors:
Dark Blue Hex: 1F2A42
Lighter Blueish Hex: 90BEC9
You're welcome to check out my website for inspiration- it is freshly created with other colors as well, and I love the outcome. www.hollowpinerest.com

Target Market(s)

Tired parents

Font styles to use
Script
Other font styles liked:
• Great Vibe, Lato or Just Another Hand are all used currently for my brand. Open to other options.

Requirements
Must have
• The letterhead (heading/footer) MUST be kept narrow (height-wise), so I have plenty of space on my document, while including important information.

It should look professional on screen, and when printed.

Must include my business name OR logo (Hollow Pine Sleep Consulting), and my email address. Mara@hollowpinerest.com

Website is optional, not required, just if you need to fill in a spot: www.hollowpinerest.com

```html
<!DOCTYPE html>
<html lang="en">
<head>
<meta charset="utf-8">
<title>Hollow Pine Sleep Consulting – Letterhead</title>
<link href="https://fonts.googleapis.com/css2?family=Lato:wght@400;700&family=Arimo:wght@700&display=swap" rel="stylesheet">
<style>
  :root {
    --navy: #1F2A42;
    --mist: #90BEC9;
    --steel: #5f8a96;
    --rule-grey: #b9bcc0;
    --ink: #2b2b2b;
    --backdrop: #e3e4e5;
    --paper: #ffffff;
  }
  html, body {
    margin: 0;
    width: 1200px;
    height: 988px;
    overflow: hidden;
    background: var(--backdrop);
  }
  .letter-page {
    position: absolute;
    left: 240px;
    top: 28px;
    width: 720px;
    height: 932px;
    background: var(--paper);
    box-shadow: 0 2px 10px rgba(0,0,0,0.12);
    overflow: hidden;
    font-family: "Lato", sans-serif;
    color: var(--ink);
  }
  .header-wave {
    position: absolute;
    top: 0;
    left: 0;
    width: 720px;
    height: 90px;
  }
  .contact-list {
    position: absolute;
    top: 9px;
    right: 26px;
    margin: 0;
    padding: 0;
    list-style: none;
    color: var(--paper);
    font-size: 10px;
    line-height: 13px;
  }
  .contact-list li {
    display: flex;
    align-items: center;
    gap: 5px;
  }
  .contact-list svg { width: 8px; height: 8px; flex: none; }
  .brand-mark {
    position: absolute;
    top: 86px;
    left: 40px;
    display: flex;
    align-items: center;
    gap: 8px;
  }
  .brand-dot {
    width: 34px;
    height: 34px;
    border-radius: 50%;
    background: var(--mist);
  }
  .brand-name {
    font-size: 15px;
    font-weight: 400;
    color: var(--navy);
    letter-spacing: 0.3px;
  }
  .letter-body {
    position: absolute;
    top: 175px;
    left: 92px;
    width: 520px;
  }
  .salutation {
    font-family: "Arimo", sans-serif;
    font-weight: 700;
    font-size: 13px;
    color: #4a4a4a;
    margin: 0 0 10px -8px;
  }
  .letter-body p.paragraph {
    font-size: 11.5px;
    line-height: 13.5px;
    text-align: justify;
    text-indent: 12px;
    margin: 0 0 20px;
  }
  .signature-area {
    position: absolute;
    top: 640px;
    left: 150px;
    width: 150px;
    height: 50px;
    background: linear-gradient(90deg, #f2f2f2, #e6e6e6);
  }
  .footer-band {
    position: absolute;
    left: 0;
    bottom: 0;
    width: 100%;
    height: 9px;
    background: var(--navy);
  }
</style>
</head>
<body>
<main class="letter-page">
  <svg class="header-wave" viewBox="0 0 720 90" preserveAspectRatio="none" aria-hidden="true">
    <defs>
      <linearGradient id="mistStripe" x1="0" x2="1" y1="0" y2="0">
        <stop offset="0" stop-color="#4d6f7b"/>
        <stop offset="0.5" stop-color="#90BEC9"/>
        <stop offset="1" stop-color="#90BEC9" stop-opacity="0.2"/>
      </linearGradient>
    </defs>
    <path d="M0 0H720V64C520 60 300 10 0 22Z" fill="var(--navy)"/>
    <path d="M0 23C300 11 520 61 720 65V67C520 64 300 22 0 33Z" fill="url(#mistStripe)"/>
    <path d="M0 36C300 25 520 67 720 69V72C520 71 300 31 0 40Z" fill="var(--rule-grey)"/>
  </svg>

  <ul class="contact-list">
    <li>
      <svg viewBox="0 0 10 10"><path d="M2 1l2 2-1 1.2c.6 1.3 1.5 2.2 2.8 2.8L7 6l2 2-1.2 1.3C4.5 9 1 5.5.7 2.2Z" fill="currentColor"/></svg>
      555-201-4830
    </li>
    <li>
      <svg viewBox="0 0 10 10"><rect x="0.5" y="2" width="9" height="6" fill="currentColor"/><path d="M0.5 2L5 5.5 9.5 2" stroke="var(--navy)" stroke-width="1" fill="none"/></svg>
      Mara@hollowpinerest.com
    </li>
    <li>
      <svg viewBox="0 0 10 10"><circle cx="5" cy="5" r="4.3" fill="currentColor"/></svg>
      www.hollowpinerest.com
    </li>
  </ul>

  <div class="brand-mark">
    <span class="brand-dot"></span>
    <span class="brand-name">Hollow Pine Sleep Consulting</span>
  </div>

  <section class="letter-body">
    <p class="salutation">Dear Mr. Avery,</p>
    <p class="paragraph">Lorem Ipsum is simply dummy text of the printing and typesetting industry. Lorem Ipsum has been the industry's standard dummy text ever since the 1500s, when an unknown printer took a galley of type and scrambled it to make a type specimen book. It has survived not only five centuries, but also the leap into electronic typesetting, remaining essentially unchanged.</p>
    <p class="paragraph">The standard chunk of Lorem Ipsum used since the 1500s is reproduced below for those interested. Sections 1.10.32 and 1.10.33 from "de Finibus Bonorum et Malorum" by Cicero are also reproduced in their exact original form, accompanied by English versions from the 1914 translation by H. Rackham</p>
    <p class="paragraph">Lorem Ipsum is simply dummy text of the printing and typesetting industry. Lorem Ipsum has been the industry's standard dummy text ever since the 1500s, when an unknown printer took a galley of type and scrambled it to make a type specimen book. It has survived not only five centuries, but also the leap into electronic typesetting, remaining essentially unchanged. It was popularised in the</p>
    <p class="paragraph">The standard chunk of Lorem Ipsum used since the 1500s is reproduced below for those interested. Sections 1.10.32 and 1.10.33 from "de Finibus Bonorum et Malorum" by Cicero are also reproduced in their exact original form, accompanied by English versions from the 1914 translation by H. Rackham</p>
  </section>

  <div class="signature-area" role="img" aria-label="Handwritten signature of the sender"></div>

  <div class="footer-band"></div>
</main>
</body>
</html>
```